Norvale Email Signature Banners – Fabrication Capability Series

www.Norvale.com.au is an Australian engineering and fabrication company specialising in fabrication and welding of :
steel piping spools,
skids and frames,
small volume process steel tanks
and general steel fabrication
We require four distinct banner designs for use in Teldrin Quillmark email signatures. Each banner will highlight a specific capability while maintaining a consistent brand identity.
Deliverables
Four banners total:
Piping Spools Fabrication – focus on precision welding and stainless steel pipework
Skid & Frames Fabrication – highlight skid systems and structural frames
Small Steel Tanks Fabrication – show fabricated tanks and workshop craftsmanship
General Fabrication Solutions – broad steel fabrication theme for company-wide use
Dimensions: 600–700 px wide × 100 px high
Format: PNG (preferred), small file size prefered
Resolution: 72 dpi
Background: non-transparent, industrial or workshop setting
Text examples:
1. Piping Spools Fabrication
Option A: “Expert Fabrication Solutions for Process Piping”
Option B: “Precision Welding for Complex Systems”
Option C: “Delivering Quality in Every Spool”
Option D: “Engineered for Flow, Built for Strength”
2. Skid & Frames Fabrication
Option A: “Custom Engineered Modular Systems”
Option B: “Built Strong. Designed Smart.”
Option C: “Reliable Frames for Industrial Performance”
Option D: “Modular Fabrication for Seamless Integration”
3. Small Steel Tanks Fabrication
Option A: “Precision Built for Your Needs”
Option B: “Compact Strength. Proven Durability.”
Option C: “Fabricated for Performance and Longevity”
Option D: “Small Tanks. Big Reliability.”
4. General Fabrication Solutions
Option A: “Quality Craftsmanship, Proven Results”
Option B: “Your Partner in Precision Fabrication”
Option C: “Engineering Excellence in Every Weld”
Option D: “Australian Fabrication. Global Standards.”
Style Direction
Clean, professional, and engineering‑focused
Use Norvale brand colours
Blend photo realism with vector clarity (no heavy gradients)
Include subtle industrial textures or workshop imagery
Typography: bold sans‑serif, legible at small scale
Usage Context
These banners will appear at the bottom of staff email signatures via Quillmark Email Signature Tool for Teldrin 365, so clarity and fast loading are essential. No Logo is required in the banners.
Reference
Existing Norvale signature is attached. Colour palette to match the signature style and logo.
Target Market(s)
Engineering and construction companies,
Industry/Entity Type
Engineering fabrication design

```html
<!DOCTYPE html>
<html lang="en">
<head>
<meta charset="utf-8">
<title>Norvale Email Signature Banners</title>
<link href="https://fonts.googleapis.com/css2?family=Poppins:wght@700;800&display=swap" rel="stylesheet">
<style>
:root{
  --sheet:#e8e8e8;
  --ink:#1d1d1d;
  --brand-blue:#0b4fad;
  --brand-blue-dark:#083f8f;
  --brand-blue-light:#1a63c4;
  --mist:#dfe6ef;
  --white:#ffffff;
}
*{margin:0;padding:0;box-sizing:border-box}
html,body{width:1200px;height:1088px;overflow:hidden;background:var(--sheet)}
body{position:relative;font-family:"Poppins",Arial,sans-serif}
.sheet-title{
  position:absolute;left:0;top:128px;width:1200px;text-align:center;
  font-weight:700;font-size:26px;letter-spacing:.5px;color:var(--ink);
}
.banner{
  position:absolute;left:167px;width:840px;height:120px;
  box-shadow:0 3px 10px rgba(0,0,0,.35);overflow:hidden;background:var(--brand-blue);
}
.banner svg{position:absolute;left:0;top:0;display:block}
.banner-headline{
  position:absolute;color:var(--white);font-weight:700;text-transform:uppercase;
  line-height:1.23;letter-spacing:.2px;
}
.banner--spools{top:236px}
.banner--skids{top:422px}
.banner--tanks{top:612px}
.banner--general{top:798px}
.banner--spools .banner-headline{left:16px;top:23px;font-size:31px}
.banner--skids .banner-headline{left:25px;top:22px;font-size:31px}
.banner--tanks .banner-headline{left:25px;top:22px;font-size:31px}
.banner--general .banner-headline{left:21px;top:26px;font-size:28px;line-height:1.3}
</style>
</head>
<body>
<h1 class="sheet-title">NORVALE EMAIL SIGNATURE BANNERS</h1>

<section class="banner banner--spools">
  <svg width="840" height="120" viewBox="0 0 840 120">
    <defs>
      <linearGradient id="spoolPhoto" x1="0" y1="0" x2="1" y2="1">
        <stop offset="0" stop-color="#c9d3dc"/>
        <stop offset=".5" stop-color="#8d99a3"/>
        <stop offset="1" stop-color="#3d4a55"/>
      </linearGradient>
    </defs>
    <rect width="840" height="120" fill="var(--brand-blue)"/>
    <g role="img" aria-label="Welder working on a large stainless steel pipe spool in the workshop">
      <polygon points="487,0 840,0 840,120 553,120 525,98 553,78 515,52 540,30 505,12" fill="url(#spoolPhoto)"/>
    </g>
    <polyline points="487,0 505,12 540,30 515,52 553,78 525,98 553,120" fill="none" stroke="var(--white)" stroke-width="4"/>
  </svg>
  <p class="banner-headline">Precision welding for<br>complex systems</p>
</section>

<section class="banner banner--skids">
  <svg width="840" height="120" viewBox="0 0 840 120">
    <defs>
      <linearGradient id="skidPhoto" x1="0" y1="0" x2="1" y2="1">
        <stop offset="0" stop-color="#b9b4ad"/>
        <stop offset=".55" stop-color="#7d7670"/>
        <stop offset="1" stop-color="#4a4540"/>
      </linearGradient>
    </defs>
    <rect width="840" height="120" fill="var(--brand-blue)"/>
    <polygon points="460,0 840,0 840,120 575,120" fill="var(--brand-blue-light)"/>
    <polygon points="480,0 840,0 840,120 560,120 520,80" fill="var(--mist)"/>
    <rect x="467" y="11" width="360" height="97" rx="9" fill="var(--white)"/>
    <g role="img" aria-label="Custom engineered modular skid system with stainless pipework and frames">
      <rect x="471" y="15" width="352" height="89" rx="6" fill="url(#skidPhoto)"/>
    </g>
  </svg>
  <p class="banner-headline">Custom engineered<br>modular systems</p>
</section>

<section class="banner banner--tanks">
  <svg width="840" height="120" viewBox="0 0 840 120">
    <defs>
      <linearGradient id="tankPhotoA" x1="0" y1="0" x2="1" y2="1">
        <stop offset="0" stop-color="#d5dbe0"/>
        <stop offset="1" stop-color="#6f7b86"/>
      </linearGradient>
      <linearGradient id="tankPhotoB" x1="0" y1="0" x2="1" y2="0">
        <stop offset="0" stop-color="#a8b0b6"/>
        <stop offset=".5" stop-color="#dfe3e6"/>
        <stop offset="1" stop-color="#8a939a"/>
      </linearGradient>
    </defs>
    <rect width="840" height="120" fill="var(--brand-blue)"/>
    <rect x="481" y="0" width="318" height="120" fill="var(--white)"/>
    <g role="img" aria-label="Technician in clean suit beside small stainless steel process tanks">
      <rect x="485" y="0" width="156" height="120" fill="url(#tankPhotoA)"/>
    </g>
    <g role="img" aria-label="Fabricated stainless steel tank in the workshop">
      <rect x="646" y="0" width="148" height="120" fill="url(#tankPhotoB)"/>
    </g>
  </svg>
  <p class="banner-headline">Precision built for<br>your needs</p>
</section>

<section class="banner banner--general">
  <svg width="840" height="120" viewBox="0 0 840 120">
    <defs>
      <radialGradient id="sparkPhoto" cx=".7" cy=".75" r=".7">
        <stop offset="0" stop-color="#e8f0ff"/>
        <stop offset=".15" stop-color="#7fa8f0"/>
        <stop offset=".5" stop-color="#1f3f86"/>
        <stop offset="1" stop-color="#0c1c3f"/>
      </radialGradient>
    </defs>
    <rect width="840" height="120" fill="var(--brand-blue)"/>
    <polygon points="490,0 840,0 840,120 466,120 466,24" fill="var(--white)"/>
    <g role="img" aria-label="Close-up of welding sparks from a gloved hand at work">
      <polygon points="494,4 836,4 836,116 470,116 470,28" fill="url(#sparkPhoto)"/>
    </g>
  </svg>
  <p class="banner-headline">Quality craftsmanship,<br>proven results</p>
</section>
</body>
</html>
```